Corporate Design für eine denkmalgeschützte Kulturstätte
Zielgruppe
Die Alte Weidenschmiede ist eine denkmalgeschützte Kulturstätte mit Museumsräumen in der Gemeinde Mühlenbecker Land. Die fast 800 Jahre alte Wassermühle wurde ursprünglich von Zisterzienser-Mönchen erbaut und liegt im Landkreis Oberhavel des Bundeslandes Brandenburg.
Am 31. März 2004 wurde aus einer Bürgerinitiative der Förderverein Al-te Weidenschmiede gegründet. Dessen Ziel war und ist es, das ruinöse Denk-mal zu restaurieren und ein kulturelles Zentrum mit Museum für die Bürger der umliegenden Gemeinden zu schaffen und Kultur-Touristen anzuziehen. Die Restaurierung wird voraussichtlich Ende 2023 abgeschlossen sein.
Der jetzige Verein Alte Weidenschmiede e.V. umfasst circa 100 Mitglieder. Ungefähr 30 Vereinsmitglieder arbeiten aktiv an der Gestaltung des Vorha-bens ehrenamtlich mit. Der Verein betreibt und organisiert:
- eine Dauer-Ausstellung im Mühlengebäude mit historischen Mühlenge-räten und Alltagsgegenständen
- zwei Kunst-Ausstellungen pro Jahr im Mühlengebäude
- ein Rastkontor, welches derzeit von Mai bis Oktober sonntags geöffnet ist
- einen Saal für Konzerte, Lesungen, Hochzeiten, Familienfeiern, Versammlungen, die Gemeinschaft stärkende Veranstaltungen, externe und interne Vereinsaktivitäten
- jährlich drei eigene Veranstaltungen: Pfingst-Lindentag, Herbst-Lindentag, Adventsmarkt
- ein Außengelände mit Wasserrad, Wasserspielplatz, Naturschutzgebiet, Lehmofen und diversen Gebäude
Zukünftig wird die Tourist-Info der Gemeinde Mühlenbecker Land in einen Teil des Gebäudes der Alten Weidenschmiede einziehen. Weiterhin ist geplant, den Museumsbetrieb zu erweitern:
- Museum zur Historie der Gemeinde, zu den Zisterzienser und zum Verein
- Ausstellung „Von Saat bis Laib“ für lebendigen Unterricht für Schul-klassen
Derzeit nutzen die Alte Weidenschmiede: Mitglieder des Vereins, Familien, Touristen, Bürger der Gemeinde, Künstler, selten Schulklassen. Zu..
Aufgabenstellung
Unser Unternehmen benötigt ein neues, einheitliches Corporate Design, das aus einem neuen Logo, einer passenden Farbpalette und Schriftarten besteht. Zusätzlich benötigen wir eine Visitenkartenvorlage sowie einen Briefkopf, die alle Elemente unseres neuen Corporate Designs enthalten.
Wir möchten gerne sicherstellen, dass unser neues Design einen Bezug zur Mühle und unserer Geschichte herstellt. Konkret möchten wir gerne das Wasserrad als Symbol integrieren sowie eine Verbindung zu den Zisterzienser-Mönchen herstellen. Als Inspiration könnten antike Türen dienen - dies ist jedoch nur eine Idee.
Möglicherweise kann die Designerin/der Designer das alte Design geschickt integrieren, um dem CD mehr Wiedererkennungswert zu verleihen.
Wir sind gespannt auf Ihre Vorschläge und freuen uns darauf, unser neues Corporate Design gemeinsam zu entwickeln.
Den Markenkern haben wir als Datei gesendet.
Die folgenden Websites/Designs gefallen uns (bitte Farben aus dem Markenkern verwenden):
- https://abtei-falkenried.de/de
- https://www.provinzsammlung.de/museum
- https://pelorian.museum/
- https://www.wirtelhaus.de/

```html
<!DOCTYPE html>
<html lang="de">
<head>
<meta charset="utf-8">
<title>Alte Weidenschmiede – Geschäftsausstattung</title>
<link rel="stylesheet" href="https://fonts.googleapis.com/css2?family=Cinzel:wght@500&family=Work+Sans:wght@400;600&display=swap">
<style>
  :root {
    --brand-red: #843430;
    --paper: #f3f3f3;
    --backdrop: #e6e6e8;
    --ink-grey: #858b93;
    --rule-grey: #6f7782;
    --white: #ffffff;
  }
  * { margin: 0; padding: 0; box-sizing: border-box; }
  html, body { width: 1200px; height: 573px; overflow: hidden; background: var(--backdrop); }
  body { position: relative; font-family: "Work Sans", Arial, sans-serif; }

  .sheet { position: absolute; background: var(--paper); overflow: hidden; }

  /* brand mark: plain circle + name */
  .mark { position: absolute; display: flex; flex-direction: column; align-items: center; color: var(--brand-red); }
  .mark-dot { border-radius: 50%; background: var(--brand-red); }
  .mark-name { font-family: "Cinzel", Georgia, serif; font-weight: 500; text-align: center; line-height: 1.05; letter-spacing: .04em; margin-top: 3px; }
  .mark--light { color: var(--white); }
  .mark--light .mark-dot { background: var(--white); }

  /* business cards */
  .card { width: 105px; height: 60px; }
  .card--red { background: var(--brand-red); }
  .card-name { position: absolute; font-family: "Cinzel", Georgia, serif; font-weight: 500; color: var(--brand-red); font-size: 4px; letter-spacing: .02em; }
  .card-role { position: absolute; font-size: 1.8px; letter-spacing: .3em; color: var(--ink-grey); text-transform: uppercase; }
  .contact { position: absolute; font-size: 2.3px; line-height: 3.4px; color: var(--brand-red); list-style: none; }
  .contact li { display: flex; align-items: center; gap: 1.5px; }
  .contact li::before { content: ""; width: 2px; height: 2px; border-radius: 50%; background: var(--rule-grey); flex: none; }
  .card-url { position: absolute; left: 0; right: 0; bottom: 2px; text-align: center; font-size: 2px; color: var(--brand-red); }
  .card-rule { position: absolute; height: .5px; background: var(--rule-grey); }

  /* envelopes */
  .envelope { width: 226px; height: 113px; }
  .envelope-flap { position: absolute; left: 0; top: 0; width: 226px; height: 28px; background: var(--brand-red); border-radius: 0 0 8px 8px / 0 0 6px 6px; }

  /* letterheads */
  .letter { width: 228px; height: 322px; }
  .letter-contact { position: absolute; font-size: 3.3px; line-height: 4.6px; color: var(--rule-grey); list-style: none; }
  .letter-contact li { display: flex; gap: 2px; }
  .letter-contact li::before { content: ""; width: 3px; height: 3px; margin-top: .6px; border-radius: 50%; background: var(--brand-red); flex: none; }
  .letter-contact--light { color: var(--white); }
  .letter-contact--light li::before { background: var(--white); }

  .footer-rules { position: absolute; left: 0; right: 0; top: 296px; }
  .footer-rules span { display: block; height: 1px; margin-bottom: 1px; }
  .footer-text { position: absolute; top: 304px; font-size: 2.6px; line-height: 4.2px; color: var(--ink-grey); }
  .footer-text b { color: var(--brand-red); font-weight: 600; }

  .band-red { position: absolute; background: var(--brand-red); }
  .header-box-title { font-family: "Cinzel", Georgia, serif; font-weight: 500; font-size: 4.2px; color: var(--white); margin-bottom: 2px; }
</style>
</head>
<body>

<!-- Business card front -->
<div class="sheet card card--red" style="left:114px;top:95px;">
  <div class="mark mark--light" style="left:0;right:0;top:12px;">
    <div class="mark-dot" style="width:18px;height:18px;"></div>
    <div class="mark-name" style="font-size:5.4px;">Alte<br>Weidenschmiede</div>
  </div>
</div>

<!-- Business card back, centred -->
<div class="sheet card" style="left:235px;top:95px;">
  <div class="mark" style="left:0;right:0;top:4px;">
    <div class="mark-dot" style="width:9px;height:9px;"></div>
    <div class="mark-name" style="font-size:3.2px;margin-top:1px;">Alte Weidenschmiede</div>
  </div>
  <div class="card-name" style="left:0;right:0;top:31px;text-align:center;">Vorname Nachname</div>
  <div class="card-role" style="left:0;right:0;top:37px;text-align:center;">Berufsbezeichnung</div>
  <ul class="contact" style="left:11px;top:42px;">
    <li>alte-weidenschmiede.de</li>
    <li>info@alte-weidenschmiede.de</li>
    <li>+49 30000 123456</li>
  </ul>
  <ul class="contact" style="left:58px;top:42px;">
    <li>Weidenweg 3,<br>16500 Lindenau</li>
  </ul>
</div>

<!-- Business card front, light -->
<div class="sheet card" style="left:114px;top:164px;">
  <div class="mark" style="left:0;right:0;top:12px;">
    <div class="mark-dot" style="width:17px;height:17px;"></div>
    <div class="mark-name" style="font-size:5px;">Alte<br>Weidenschmiede</div>
  </div>
  <div class="card-rule" style="left:0;right:0;bottom:5px;"></div>
  <div class="card-url">alte-weidenschmiede.de</div>
</div>

<!-- Business card back, right aligned mark -->
<div class="sheet card" style="left:235px;top:164px;">
  <div class="mark" style="right:9px;top:5px;">
    <div class="mark-dot" style="width:11px;height:11px;"></div>
    <div class="mark-name" style="font-size:3.2px;margin-top:1px;">Alte Weidenschmiede</div>
  </div>
  <div class="card-name" style="left:12px;top:28px;">Vorname Nachname</div>
  <div class="card-role" style="left:12px;top:34px;">Berufsbezeichnung</div>
  <div class="card-rule" style="left:12px;right:0;top:37px;"></div>
  <ul class="contact" style="left:11px;top:41px;">
    <li>alte-weidenschmiede.de</li>
    <li>info@alte-weidenschmiede.de</li>
    <li>+49 30000 123456</li>
  </ul>
  <ul class="contact" style="left:58px;top:41px;">
    <li>Weidenweg 3,<br>16500 Lindenau</li>
  </ul>
</div>

<!-- Envelope, front -->
<div class="sheet envelope" style="left:114px;top:240px;">
  <div class="mark" style="left:12px;top:10px;">
    <div class="mark-dot" style="width:22px;height:22px;"></div>
    <div class="mark-name" style="font-size:5.6px;">Alte<br>Weidenschmiede</div>
  </div>
</div>

<!-- Envelope, back with flap -->
<div class="sheet envelope" style="left:114px;top:372px;">
  <div class="envelope-flap"></div>
  <div class="mark" style="left:0;right:0;top:48px;">
    <div class="mark-dot" style="width:24px;height:24px;"></div>
    <div class="mark-name" style="font-size:6.4px;">Alte<br>Weidenschmiede</div>
  </div>
</div>

<!-- Letterhead 1: centred mark, footer -->
<div class="sheet letter" style="left:363px;top:130px;">
  <div class="mark" style="left:0;right:0;top:18px;">
    <div class="mark-dot" style="width:28px;height:28px;"></div>
    <div class="mark-name" style="font-size:7.2px;">Alte<br>Weidenschmiede</div>
  </div>
  <div class="footer-rules">
    <span style="background:var(--brand-red);"></span>
    <span style="background:var(--rule-grey);"></span>
  </div>
  <div class="footer-text" style="left:14px;"><b>Adresse:</b> Weidenweg 3,<br>16500 Lindenau</div>
  <div class="footer-text" style="left:82px;"><b>Tel.:</b> +49 30000 123456<br><b>Web:</b> alte-weidenschmiede.de<br><b>Mail:</b> info@alte-weidenschmiede.de</div>
  <div class="footer-text" style="left:158px;"><b>BANK</b> BANK BANK BANK<br><b>IBAN</b> DE90 1234 1234 1234 1234 12<br><b>BIC</b> BICBICBIC</div>
</div>

<!-- Letterhead 2: left mark with contact list -->
<div class="sheet letter" style="left:608px;top:130px;">
  <div class="mark" style="left:21px;top:12px;">
    <div class="mark-dot" style="width:30px;height:30px;"></div>
    <div class="mark-name" style="font-size:7.6px;">Alte<br>Weidenschmiede</div>
  </div>
  <ul class="letter-contact" style="left:21px;top:65px;">
    <li>Weidenweg 3,<br>16500 Lindenau</li>
    <li>alte-weidenschmiede.de</li>
    <li>info@alte-weidenschmiede.de</li>
    <li>+49 30000 123456</li>
  </ul>
  <div class="band-red" style="left:0;right:0;bottom:0;height:5px;"></div>
</div>

<!-- Letterhead 3: red header bands -->
<div class="sheet letter" style="left:846px;top:130px;">
  <div class="band-red" style="left:0;top:13px;width:28px;height:38px;"></div>
  <div class="mark" style="left:35px;top:13px;">
    <div class="mark-dot" style="width:22px;height:22px;"></div>
    <div class="mark-name" style="font-size:5.8px;">Alte<br>Weidenschmiede</div>
  </div>
  <div class="band-red" style="left:92px;right:0;top:13px;height:38px;padding:3px 0 0 37px;">
    <div class="header-box-title">Alte Weidenschmiede e.V.</div>
    <ul class="letter-contact letter-contact--light" style="position:static;font-size:2.9px;line-height:4.2px;">
      <li>Weidenweg 3,<br>16500 Lindenau</li>
      <li>alte-weidenschmiede.de</li>
      <li>info@alte-weidenschmiede.de</li>
      <li>+49 30000 123456</li>
    </ul>
  </div>
  <div class="band-red" style="left:0;right:0;bottom:4px;height:1px;"></div>
  <div class="band-red" style="left:0;right:0;bottom:0;height:2px;"></div>
</div>

</body>
</html>
```